依頼詳細
頂いている参考サイトとしては下記のURLがありますが、
先方でもどのデザインの何が良いのかは計りかねているらしく、
下記を参考に様々な形式でデザインを作成して欲しいということです。

‣BRIGHTLEAF https://www.brightleaf57.jp/biwako-sup/ ➡デザインが素敵
‣丸岡商 https://www.maruokasho.co.jp/ja/ ➡ 大企業感
‣ひらめき工房本部 https://www.hiramekikobo.jp/  ➡ 同コンセプト

また、事業内容は現在のページに準拠するということで、現在サイトのパスはpemixとなります。

TOPページへの掲載内容については、
TOPイメージ
事業内容
採用情報
新着情報
となります。
サイトURL
http://nexal.co.jp/
ページ数
1ページ
希望イメージ
シンプル 複雑
単色 カラフル
暗い 明るい
日常 高級
遊び心 厳粛
未来的 伝統的
女性的 男性的
希望する色
緑系
納品ファイル
• フォトショップ形式 (.psd)
補足説明
依頼公開後の追記内容
現行サイトのパスワードについて失念しておりました。
パスワードは pemix となります。
■ 選んだ理由

デザインが特に先方に気に入られたため

■ 提案者全員のお礼・コメント

この度はご提案をいただきまして、誠にありがとうございました。
また機会がありましたら、よろしくお願い致します。

```html
<!DOCTYPE html>
<html lang="ja">
<head>
<meta charset="utf-8">
<title>株式会社ソラテック</title>
<link href="https://fonts.googleapis.com/css2?family=Noto+Sans+JP:wght@400;500;700&family=Noto+Serif+JP:wght@500;700&family=Montserrat:wght@500;600;700&display=swap" rel="stylesheet">
<style>
:root{
  --green:#1aa35a;
  --green-dark:#128a4a;
  --green-soft:#e6f5ec;
  --ink:#333;
  --muted:#777;
  --grey-bg:#f3f4f4;
  --line:#e2e2e2;
  --white:#fff;
}
*{margin:0;padding:0;box-sizing:border-box}
html,body{width:1200px;height:3196px;overflow:hidden}
body{font-family:"Noto Sans JP",sans-serif;color:var(--ink);background:var(--white);position:relative}
.abs{position:absolute}
.photo{position:absolute}

/* header */
.site-header{position:absolute;top:0;left:0;width:1200px;height:88px;z-index:5;display:flex;align-items:center;justify-content:space-between;padding-left:40px}
.brand{display:flex;align-items:center;gap:12px;font-weight:700;font-size:22px;color:var(--ink);white-space:nowrap}
.brand-mark{width:24px;height:24px;background:var(--green);border-radius:50%}
.global-nav{display:flex;height:88px}
.global-nav a{width:150px;display:flex;flex-direction:column;align-items:center;justify-content:center;text-decoration:none;color:var(--ink);font-size:15px;font-weight:500;gap:4px}
.global-nav a span{font-family:Montserrat,sans-serif;font-size:10px;color:var(--muted);letter-spacing:.08em}
.global-nav a.is-current{background:var(--green);color:#fff}
.global-nav a.is-current span{color:#d7f2e2}

/* hero */
.hero{left:0;top:0;width:1200px;height:640px;background:linear-gradient(100deg,#f4f7f9 0%,#e9eef2 45%,#d8e0e6 100%)}
.hero-copy{left:110px;top:250px;font-family:"Noto Serif JP",serif;font-weight:700;font-size:38px;line-height:1.8;color:var(--ink);letter-spacing:.08em}

/* section titles */
.section-title{font-family:Montserrat,sans-serif;font-weight:700;color:var(--green);letter-spacing:.08em}
.section-sub{font-size:13px;color:var(--ink)}
.service-head{left:0;top:750px;width:1200px;text-align:center}
.service-head .section-title{font-size:34px}
.service-head .section-sub{margin-top:6px}

/* service cards */
.service-card{background:#fff;border-radius:10px;box-shadow:0 6px 24px rgba(0,0,0,.12);padding:26px 30px;width:340px}
.card-label{font-family:Montserrat,sans-serif;font-size:13px;color:var(--green);letter-spacing:.05em}
.card-icon{width:40px;height:40px;border-radius:6px;margin:12px auto 10px}
.card-title{font-size:22px;font-weight:700;text-align:center}
.card-text{font-size:13px;line-height:1.7;text-align:center;color:var(--ink);margin-top:10px}
.pill-btn{display:flex;align-items:center;justify-content:space-between;width:170px;height:40px;border:2px solid var(--green);border-radius:20px;padding:0 8px 0 24px;font-size:13px;color:var(--green-dark);margin:18px auto 0;background:#fff}
.pill-btn i{width:24px;height:24px;border-radius:50%;background:var(--green);display:flex;align-items:center;justify-content:center}

/* news */
.news{left:0;top:1720px;width:1200px;height:360px;background:var(--grey-bg)}
.news-head{left:200px;top:1800px}
.news-head .section-title{font-size:34px}
.news-list{left:560px;top:1780px;width:520px}
.news-item{margin-bottom:26px}
.news-item time{display:block;font-family:Montserrat,sans-serif;font-size:13px;color:var(--green)}
.news-item p{font-size:14px;line-height:1.7;margin-top:4px}

/* recruit */
.recruit-text{left:710px;top:2240px;width:420px}
.recruit-text .section-title{font-size:34px}
.recruit-lead{font-size:14px;color:var(--green-dark);margin:18px 0 8px;font-weight:500}
.recruit-body{font-size:13px;line-height:1.8}

/* contact */
.contact-bar{left:160px;top:2660px;width:900px;height:140px;border-radius:70px;background:#fff;box-shadow:0 6px 30px rgba(0,0,0,.1);display:flex;align-items:center;padding:0 70px}
.contact-bar .icon-box{width:54px;height:34px;background:var(--green-soft);border-radius:4px;margin-right:40px}
.contact-bar .section-title{font-size:28px;color:var(--ink)}
.contact-bar .note{margin-left:auto;font-size:14px;margin-right:24px}
.circle-arrow{width:30px;height:30px;border-radius:50%;background:var(--green);display:flex;align-items:center;justify-content:center}

/* footer */
.site-footer{left:0;top:2870px;width:1200px;height:326px}
.footer-brand{left:120px;top:40px}
.footer-address{left:120px;top:110px;font-size:13px;line-height:1.8}
.footer-nav{left:1000px;top:40px;list-style:none;font-family:Montserrat,sans-serif;font-size:13px}
.footer-nav li{padding:6px 0;border-bottom:1px solid var(--line);width:100px}
.copyright{left:120px;top:240px;font-size:12px;color:var(--muted)}
.footer-band{left:0;top:300px;width:1200px;height:26px;background:var(--green)}
</style>
</head>
<body>

<div class="photo hero" role="img" aria-label="明るいオフィスで胸に手を当てて微笑むスーツ姿の女性"></div>

<header class="site-header">
  <div class="brand"><span class="brand-mark"></span>株式会社ソラテック</div>
  <nav class="global-nav">
    <a class="is-current" href="#">ホーム<span>HOME</span></a>
    <a href="#">事業内容<span>SERVICE</span></a>
    <a href="#">会社概要<span>COMPANY</span></a>
    <a href="#">採用情報<span>RECRUIT</span></a>
    <a href="#">お問い合わせ<span>CONTACT</span></a>
  </nav>
</header>

<h1 class="abs hero-copy">好奇と勇気に知恵を<br>合わせれば、<br>何事も永続につながる</h1>

<div class="abs service-head">
  <h2 class="section-title">SERVICE</h2>
  <p class="section-sub">株式会社ソラテックの事業内容をご紹介します。</p>
</div>

<div class="photo" style="left:0;top:872px;width:1200px;height:416px;background:linear-gradient(90deg,#cfd6dc,#e6eaee)" role="img" aria-label="オフィスに立つスーツ姿の男女"></div>
<div class="abs service-card" style="left:760px;top:930px">
  <div class="card-label">Service — 01</div>
  <div class="card-icon" style="background:#2f8fd0"></div>
  <div class="card-title">教育事業部</div>
  <p class="card-text">個別指導の教室運営を通じて<br>子どもの学ぶ力を育てています</p>
  <div class="pill-btn">詳しく見る<i><svg width="10" height="10" viewBox="0 0 10 10"><path d="M3 1l4 4-4 4" stroke="#fff" stroke-width="1.6" fill="none"/></svg></i></div>
</div>

<div class="photo" style="left:0;top:1320px;width:1200px;height:380px;background:linear-gradient(90deg,#f2f3f4,#c9cfd5)" role="img" aria-label="会議室で打ち合わせをするビジネスパーソン"></div>
<div class="abs service-card" style="left:60px;top:1370px">
  <div class="card-label">Service — 02</div>
  <div class="card-icon" style="background:#d94848"></div>
  <div class="card-title">日泰事業部</div>
  <p class="card-text">日本とタイの交流を通じて<br>新しい価値を生み出しています</p>
  <div class="pill-btn">詳しく見る<i><svg width="10" height="10" viewBox="0 0 10 10"><path d="M3 1l4 4-4 4" stroke="#fff" stroke-width="1.6" fill="none"/></svg></i></div>
</div>

<section class="abs news"></section>
<div class="abs news-head">
  <h2 class="section-title">NEWS</h2>
  <p class="section-sub" style="margin-top:6px">当社からのお知らせです。</p>
  <div class="pill-btn" style="margin:30px 0 0;width:120px;height:34px">一覧<i><svg width="10" height="10" viewBox="0 0 10 10"><path d="M3 1l4 4-4 4" stroke="#fff" stroke-width="1.6" fill="none"/></svg></i></div>
</div>
<div class="abs news-list">
  <div class="news-item"><time>2020.03.20</time><p>企業のお知らせです。ホームページを公開しました。</p></div>
  <div class="news-item"><time>2020.03.10</time><p>企業のお知らせです。採用情報を更新しました。</p></div>
  <div class="news-item"><time>2020.03.01</time><p>オフィスのリニューアルが完了しました。新しいオフィスで<br>皆さまのお越しをお待ちしています。</p></div>
</div>

<div class="photo" style="left:0;top:2120px;width:660px;height:400px;background:linear-gradient(90deg,#d6dde3,#eef1f3)" role="img" aria-label="並んで立つスーツ姿の社員たち"></div>
<div class="abs recruit-text">
  <h2 class="section-title">RECRUIT</h2>
  <p class="section-sub" style="margin-top:6px">一緒に働く仲間を募集しています。</p>
  <p class="recruit-lead">求めるのは大人力</p>
  <p class="recruit-body">自分の可能性を信じ、新しいことに挑戦し続けられる方を求めています。仲間と協力しながら、ともに成長していける職場です。</p>
  <div class="pill-btn" style="margin:24px 0 0 auto">詳しく見る<i><svg width="10" height="10" viewBox="0 0 10 10"><path d="M3 1l4 4-4 4" stroke="#fff" stroke-width="1.6" fill="none"/></svg></i></div>
</div>

<div class="abs contact-bar">
  <span class="icon-box"></span>
  <h2 class="section-title">CONTACT</h2>
  <span class="note">お気軽にご連絡ください。</span>
  <span class="circle-arrow"><svg width="12" height="12" viewBox="0 0 10 10"><path d="M3 1l4 4-4 4" stroke="#fff" stroke-width="1.6" fill="none"/></svg></span>
</div>

<footer class="abs site-footer">
  <div class="abs footer-brand brand"><span class="brand-mark"></span>株式会社ソラテック</div>
  <p class="abs footer-address">本社所在<br>TOWN 000<br>架空県架空市中央町1-2-3 サンプルビル5F</p>
  <ul class="abs footer-nav">
    <li>HOME</li><li>SERVICE</li><li>COMPANY</li><li>RECRUIT</li><li>CONTACT</li>
  </ul>
  <p class="abs copyright">© 株式会社ソラテック</p>
  <div class="abs footer-band"></div>
</footer>

</body>
</html>
```